Web Design Front Page Only for Organic Skincare

We have been in business for nearly 20 years. We are run by all females and sell anything from aromatherapy, skincare and pharmacy types products to health food shops and pharmacy. We are looking for an attractive and colourful but simple front web page design for our wholesale customers to look at. We want our customers to start using our website to find information rather than ringing us. So we want it to be attractive to our buyers who are young and funky.
Updates

To give you an idea of the products we sell to pharmacy and health food shops also beauty shops and hair salons.  We mainly deal with organic body and skincare, aromatherapy oils and body products, but also do some simple pharmacy products such as bandages and pill boxes, finger splits, walking frames and wheelchairs.  We are only looking for the front page of the website.  The back-end will be done in-house.  We currently do not have a logo designed so I am thinking that once we have done the website design we can build a logo from it.  I like bright colours and want something that is inviting to further discover that we do many different types of products.

Target Market(s)

young girls who are our retail buyers

Industry/Entity Type

Pharmacy

Requirements
Must have
• A section which says

Customer Log in
Should not have
• don't worry about too much writing or tabs. We will insert these later. Just come up with design image.

```html
<!DOCTYPE html>
<html lang="en">
<head>
<meta charset="utf-8">
<title>Leafmere Healthcare</title>
<link href="https://fonts.googleapis.com/css2?family=Raleway:wght@400&family=Roboto+Condensed:wght@700&family=Dosis:wght@400&family=Arial&display=swap" rel="stylesheet">
<style>
  :root {
    --bg-top: #6fd173;
    --bg-bottom: #b3f6ad;
    --nav: #4fad4b;
    --nav-active: #3f9a3c;
    --sidebar: #4fac4a;
    --panel: #b6f6b3;
    --footer: #3a9a37;
    --button: #4aaa46;
    --text-light: #ffffff;
    --text-product: #6b7a6b;
    --leaf-a: #9ed82a;
    --leaf-b: #4e9a12;
    --lavender-a: #6a4fa8;
    --lavender-b: #4f7a3a;
    --grass-a: #2c6a1e;
    --grass-b: #86c84a;
  }
  * { margin: 0; padding: 0; box-sizing: border-box; }
  html, body { width: 943px; height: 1200px; overflow: hidden; }
  body {
    position: relative;
    background: linear-gradient(to bottom, var(--bg-top) 0%, var(--bg-top) 45%, var(--bg-bottom) 100%);
    font-family: "Roboto Condensed", sans-serif;
  }
  .brand {
    position: absolute; left: 130px; top: 72px;
    font-family: "Raleway", sans-serif; font-weight: 400;
    font-size: 33px; letter-spacing: 2.5px; color: var(--text-light);
    text-transform: uppercase; white-space: nowrap;
  }
  .account {
    position: absolute; left: 664px; top: 72px; width: 180px; height: 29px;
    display: flex; box-shadow: 0 2px 3px rgba(0,0,0,.15);
  }
  .account a {
    flex: 1; display: flex; align-items: center; justify-content: center;
    background: linear-gradient(#8fdc8c, #6cc469);
    color: var(--text-light); text-decoration: none;
    font-family: Arial, sans-serif; font-size: 12px;
  }
  .account a + a { border-left: 1px solid #5bb458; }
  .shadow-band {
    position: absolute; left: 0; top: 196px; width: 943px; height: 20px;
    background: linear-gradient(to bottom, rgba(60,150,60,0) 0%, rgba(60,150,60,.45) 100%);
  }
  .main-nav {
    position: absolute; left: 129px; top: 157px; width: 715px; height: 57px;
    background: var(--nav); display: flex;
  }
  .main-nav a {
    display: flex; align-items: center; justify-content: center;
    color: var(--text-light); text-decoration: none; font-size: 15.5px;
    text-transform: uppercase; position: relative;
  }
  .main-nav a.active { background: var(--nav-active); }
  .main-nav a + a::before {
    content: ""; position: absolute; left: 0; top: 10px; bottom: 10px;
    border-left: 1px dotted rgba(255,255,255,.5);
  }
  .main-nav a.active::before, .main-nav a.active + a::before { display: none; }
  .hero {
    position: absolute; left: 129px; top: 214px; width: 715px; height: 280px;
    display: flex; box-shadow: 0 8px 30px rgba(30,120,30,.45);
  }
  .hero div { height: 100%; }
  .hero .leaf { width: 226px; background: linear-gradient(135deg, var(--leaf-a), var(--leaf-b)); }
  .hero .lavender { width: 237px; background: linear-gradient(to bottom, #5a3a3a 0%, var(--lavender-a) 40%, var(--lavender-b) 100%); }
  .hero .grass { width: 252px; background: linear-gradient(100deg, var(--grass-a), var(--grass-b) 55%, var(--grass-a)); }
  .categories {
    position: absolute; left: 129px; top: 518px; width: 228px; height: 311px;
    background: var(--sidebar); list-style: none; padding: 10px 13px 0;
  }
  .categories li {
    height: 42.6px; display: flex; align-items: center; justify-content: center;
    color: var(--text-light); font-size: 15.5px; text-transform: uppercase;
    border-bottom: 1px dotted rgba(255,255,255,.6);
  }
  .categories li:last-child { border-bottom: none; }
  .products {
    position: absolute; left: 379px; top: 517px; width: 465px; height: 490px;
    background: var(--panel);
  }
  .products .divider {
    position: absolute; left: 12px; top: 252px; width: 442px;
    border-top: 1px dotted #6a9a6a;
  }
  .product { position: absolute; width: 200px; }
  .product .photo {
    width: 56px; height: 143px; margin-left: 35px;
    background: linear-gradient(to right, #dcdcdc, #ffffff 45%, #d8d8d8);
    border-radius: 6px 6px 14px 14px;
  }
  .product .name {
    margin-top: 19px; font-family: "Dosis", sans-serif; font-size: 12.5px;
    color: var(--text-product); text-transform: uppercase;
  }
  .product .price {
    margin-top: 5px; font-family: "Dosis", sans-serif; font-size: 12.5px;
    color: var(--text-product);
  }
  .product .add {
    margin-top: 5px; width: 96px; height: 15px; background: var(--button);
    color: #e8fbe6; font-family: "Dosis", sans-serif; font-size: 12px;
    display: flex; align-items: center; justify-content: center; text-transform: uppercase;
  }
  .footer-nav {
    position: absolute; left: 138px; top: 1124px; width: 668px; height: 48px;
    background: var(--footer); display: flex; align-items: center; justify-content: center;
    font-family: Arial, sans-serif; font-size: 8.5px; color: var(--text-light);
  }
  .footer-nav a { color: var(--text-light); text-decoration: none; padding: 0 8px; }
  .footer-nav a + a { border-left: 1px solid var(--text-light); }
</style>
</head>
<body>
  <div class="brand">Leafmere Healthcare</div>

  <nav class="account">
    <a href="#">Log in</a>
    <a href="#">Register</a>
  </nav>

  <div class="shadow-band"></div>

  <nav class="main-nav">
    <a href="#" style="width:117px">About us</a>
    <a href="#" style="width:120px">Health food</a>
    <a href="#" class="active" style="width:105px">Pharmacy</a>
    <a href="#" style="width:119px">Supermarket</a>
    <a href="#" style="width:98px">Beauty</a>
    <a href="#" style="width:156px">Contact us</a>
  </nav>

  <section class="hero">
    <div class="leaf" role="img" aria-label="Close-up photo of a bright green leaf"></div>
    <div class="lavender" role="img" aria-label="Photo of purple lavender flowers"></div>
    <div class="grass" role="img" aria-label="Photo of grass blades with dew drops"></div>
  </section>

  <ul class="categories">
    <li>Face care</li>
    <li>Hair care</li>
    <li>Fragrance</li>
    <li>Bath &amp; body</li>
    <li>Face care</li>
    <li>Hair care</li>
    <li>Fragrance</li>
  </ul>

  <section class="products">
    <article class="product" style="left:45px; top:13px">
      <div class="photo" role="img" aria-label="Product photo of a white cream tube"></div>
      <p class="name">Precious cream 50 ml</p>
      <p class="price">70$</p>
      <div class="add">Add to bag</div>
    </article>
    <article class="product" style="left:268px; top:13px">
      <div class="photo" role="img" aria-label="Product photo of a white cream tube"></div>
      <p class="name">Precious cream 50 ml</p>
      <p class="price">70$</p>
      <div class="add">Add to bag</div>
    </article>
    <div class="divider"></div>
    <article class="product" style="left:45px; top:262px">
      <div class="photo" role="img" aria-label="Product photo of a white cream tube"></div>
      <p class="name">Precious cream 50 ml</p>
      <p class="price">70$</p>
      <div class="add">Add to bag</div>
    </article>
    <article class="product" style="left:266px; top:262px">
      <div class="photo" role="img" aria-label="Product photo of a white cream tube"></div>
      <p class="name">Precious cream 50 ml</p>
      <p class="price">70$</p>
      <div class="add">Add to bag</div>
    </article>
  </section>

  <footer class="footer-nav">
    <a href="#">About us</a>
    <a href="#">Health food</a>
    <a href="#">Pharmacy</a>
    <a href="#">Supermarket</a>
    <a href="#">Beauty</a>
    <a href="#">Contact us</a>
  </footer>
</body>
</html>
```